Business card like design

Hello we need a business card like design, not with personal info. But with info from our shop, like address, phone, street, email, facebook .....
This cards we put in the box when we send out the orders......
Target Market(s)
We sell cheap sunglasses, our customers are mainly young adults, that like going to parties
Industry/Entity Type
Business

```html
<!DOCTYPE html>
<html lang="en">
<head>
<meta charset="utf-8">
<title>Bright Shades – shop card</title>
<link rel="stylesheet" href="https://fonts.googleapis.com/css2?family=Fira+Sans+Condensed:wght@500&display=swap">
<style>
  :root {
    --backdrop: #ecebea;
    --card-front: #c4c4c4;
    --card-back-top: #2c2d2f;
    --card-back-bottom: #18191a;
    --copper: #b27b42;
    --copper-deep: #8a5a2c;
    --ink-light: #eeeeee;
    --ink-dark: #1d1d1e;
    --sun: #d98a3a;
  }
  * { margin: 0; padding: 0; box-sizing: border-box; }
  html, body {
    width: 1200px;
    height: 853px;
    overflow: hidden;
    background: var(--backdrop);
    font-family: "Fira Sans Condensed", "Arial Narrow", sans-serif;
  }
  .sheet {
    position: relative;
    width: 1200px;
    height: 853px;
  }
  .card {
    position: absolute;
    top: 266px;
    width: 560px;
    height: 320px;
    box-shadow: 0 6px 18px rgba(0,0,0,0.18);
  }
  .card--front {
    left: 20px;
    background: var(--card-front);
    display: flex;
    align-items: center;
    justify-content: center;
    gap: 14px;
  }
  .card--back {
    left: 620px;
    background: linear-gradient(180deg, var(--card-back-top), var(--card-back-bottom));
  }
  .brand-dot {
    width: 30px;
    height: 30px;
    border-radius: 50%;
    background: var(--sun);
    flex: none;
  }
  .brand-name {
    font-weight: 500;
    letter-spacing: 0.5px;
  }
  .card--front .brand-name {
    font-size: 44px;
    color: var(--ink-dark);
  }
  .back-brand {
    position: absolute;
    left: 60px;
    top: 142px;
    display: flex;
    align-items: center;
    gap: 8px;
  }
  .back-brand .brand-dot { width: 18px; height: 18px; }
  .card--back .brand-name {
    font-size: 22px;
    color: var(--copper);
  }
  .divider {
    position: absolute;
    left: 262px;
    top: 66px;
    width: 5px;
    height: 172px;
    border-left: 1px solid var(--copper);
    border-right: 1px solid var(--copper-deep);
  }
  .contact {
    position: absolute;
    left: 278px;
    top: 106px;
    list-style: none;
    font-size: 14.5px;
    font-weight: 500;
    line-height: 18px;
    letter-spacing: 0.4px;
  }
  .contact .address { color: var(--copper); }
  .contact .line { color: var(--ink-light); }
</style>
</head>
<body>
  <main class="sheet">
    <section class="card card--front" aria-label="Card front">
      <span class="brand-dot"></span>
      <span class="brand-name">brightshades.nl</span>
    </section>

    <section class="card card--back" aria-label="Card back">
      <div class="back-brand">
        <span class="brand-dot"></span>
        <span class="brand-name">brightshades.nl</span>
      </div>
      <div class="divider"></div>
      <ul class="contact">
        <li class="address">Address: Havenkade 14</li>
        <li class="address">4811 KL Breda, Nederland</li>
        <li class="line">E-Mail: Info@BrightShades.nl</li>
        <li class="line">Phone: 40 55 612 47 0031</li>
        <li class="line">facebook.com/brightshades</li>
      </ul>
    </section>
  </main>
</body>
</html>
```